I need a business Card Design for my practice , i am clinical herbalist. I am a herbalist specializing in Lyme disease, autism, autoimmune diseases, difficult to cure diseasesDifficult to cure diseases. In my innovative practice i link traditional medicine, herbs with science, immunologu ,pharmacology.

Industry/Entity Type

Business

Contact Information for Business Card

My company name : OŚRODEK ZIELNIK
My name : Piotr Kaleta
Name of my profession : Fitoterapeuta
In Polish language Fitoterapeuta is Herbalist .

e-mail: piotrkaleta@osrodekzielnik.com
www.osrodek-zielnik.pl
phone : 604 587 231
My company adress : Dąbrowa Sitnicka 41 , 38-415 Lużna
I dont have logo .

Requirements
Nice to have
• My company

```html
<!DOCTYPE html>
<html lang="pl">
<head>
<meta charset="utf-8">
<title>Ośrodek Zielnik – wizytówka</title>
<link rel="stylesheet" href="https://fonts.googleapis.com/css2?family=Open+Sans:wght@400;700;800&display=swap">
<style>
  :root {
    --backdrop: #e4e4e1;
    --paper: #f6f7f6;
    --leaf: #77c152;
    --charcoal: #282d2a;
    --ink: #0a0a0a;
    --white: #ffffff;
  }
  * { box-sizing: border-box; margin: 0; padding: 0; }
  html, body {
    width: 1200px; height: 1135px; overflow: hidden;
    background: var(--backdrop);
    font-family: "Open Sans", Arial, sans-serif;
  }
  .card {
    position: absolute; left: 237px;
    width: 680px; height: 406px;
    background: var(--paper);
    box-shadow: 0 10px 26px rgba(0,0,0,0.18);
    overflow: hidden;
  }
  .card--front { top: 90px; }
  .card--back { top: 625px; }

  .brand-name {
    font-weight: 800; color: var(--ink);
    text-align: center; line-height: 1.08;
    letter-spacing: 0.5px;
  }
  .card--front .brand-name {
    position: absolute; left: 0; top: 0;
    width: 360px; height: 406px;
    display: flex; align-items: center; justify-content: center;
    font-size: 42px;
  }
  .card--back .brand-name {
    position: absolute; left: 0; top: 0;
    width: 680px; height: 350px;
    display: flex; align-items: center; justify-content: center;
    font-size: 50px;
  }

  .contact-panel {
    position: absolute; left: 360px; top: 0;
    width: 320px; height: 406px;
    background: var(--leaf);
  }
  .holder-name {
    position: absolute; left: 38px; top: 24px;
    color: var(--white); font-weight: 700; font-size: 27px; letter-spacing: 0.5px;
  }
  .holder-role {
    position: absolute; left: 38px; top: 73px;
    color: var(--white); font-size: 13px;
  }
  .contact-row {
    position: absolute; left: 0; width: 320px; height: 57px;
    background: var(--charcoal);
    display: flex; align-items: center;
    padding-left: 38px; gap: 10px;
    color: var(--white); font-size: 14px;
  }
  .contact-row .notch { position: absolute; left: 0; top: 0; }
  .contact-row--phone { top: 180px; }
  .contact-row--mail { top: 252px; }
  .contact-row--web { top: 324px; }
  .contact-icon { width: 18px; height: 18px; flex: none; }

  .back-band {
    position: absolute; left: 0; bottom: 0;
    width: 680px; height: 56px; background: var(--leaf);
  }
</style>
</head>
<body>

<section class="card card--front" aria-label="Przód wizytówki">
  <div class="brand-name">OŚRODEK<br>ZIELNIK</div>

  <div class="contact-panel">
    <div class="holder-name">PIOTR KALETA</div>
    <div class="holder-role">Fitoterapeuta</div>

    <div class="contact-row contact-row--phone">
      <svg class="notch" width="20" height="57" viewBox="0 0 20 57"><polygon points="0,0 16,28.5 0,57" fill="var(--paper)"/></svg>
      <svg class="contact-icon" viewBox="0 0 18 18"><circle cx="9" cy="9" r="9" fill="var(--leaf)"/><path d="M6.2 4.6c.4-.3.9-.2 1.1.2l.9 1.7c.2.4.1.8-.2 1.1l-.6.5c.5 1.1 1.3 2 2.4 2.5l.5-.6c.3-.3.8-.4 1.1-.2l1.7.9c.4.2.5.8.2 1.1l-.7.9c-.5.6-1.4.7-2.1.4-2.2-1-3.9-2.7-4.9-4.9-.3-.7-.2-1.6.4-2.1z" fill="var(--white)"/></svg>
      <span>604 587 231</span>
    </div>

    <div class="contact-row contact-row--mail">
      <svg class="notch" width="20" height="57" viewBox="0 0 20 57"><polygon points="0,0 16,28.5 0,57" fill="var(--paper)"/></svg>
      <svg class="contact-icon" viewBox="0 0 18 18"><circle cx="9" cy="9" r="9" fill="var(--leaf)"/><rect x="4.5" y="5.8" width="9" height="6.4" rx="0.8" fill="var(--white)"/><path d="M4.8 6.2 9 9.3l4.2-3.1" fill="none" stroke="var(--leaf)" stroke-width="0.9"/></svg>
      <span>piotrkaleta@osrodekzielnik.com</span>
    </div>

    <div class="contact-row contact-row--web">
      <svg class="notch" width="20" height="57" viewBox="0 0 20 57"><polygon points="0,0 16,28.5 0,57" fill="var(--paper)"/></svg>
      <svg class="contact-icon" viewBox="0 0 18 18"><circle cx="9" cy="9" r="9" fill="var(--leaf)"/><g fill="none" stroke="var(--white)" stroke-width="0.9"><circle cx="9" cy="9" r="4.6"/><ellipse cx="9" cy="9" rx="2" ry="4.6"/><path d="M4.4 9h9.2M5 6.7h8M5 11.3h8"/></g></svg>
      <span>www.osrodek-zielnik.pl</span>
    </div>
  </div>
</section>

<section class="card card--back" aria-label="Tył wizytówki">
  <div class="brand-name">OŚRODEK<br>ZIELNIK</div>
  <div class="back-band"></div>
</section>

</body>
</html>
```